Design for Gourmet Chocolate e-Commerce Website
Detailed Instructions
Creative Brief
Company sells Gourmet Chocolate, Truffles & Chocolate Gift Baskets
1) I like the color scheme of http://www.brambleforkconfections.example/ 2) This new website that we are creating will be a franchise and sell items from velvetcocoabox.example. You can use any images and items on velvetcocoabox.example 3) I like the category page layout of http://www.tulipcrate.example/gifts-her-rfffv?ref=HomeNoRef&navContent=T%3afor+her%3a&navLocation=T%3a3-9%3a
Clean/Simple
white/grey
light brown
dark brown
left side
http://pembrokehalsey.example/
http://www.truffleden.example/
http://www.orchardmerrytaste.example/
1) The following pages need to be designed Homepage Category Page Product Detail Page Shopping Cart Page Checkout Page CMS page 2) Website has only these categories Gift Boxes Gift Baskets Gift Treys Dairy Free Sugar Free Bulk Confections

```html
<!DOCTYPE html>
<html lang="en">
<head>
<meta charset="utf-8">
<title>Checkout – Maison Brunelle</title>
<link href="https://fonts.googleapis.com/css2?family=Arimo:wght@400;700&family=PT+Serif:wght@400;700&display=swap" rel="stylesheet">
<style>
:root{
  --cocoa-dark:#3d1c0c;
  --cocoa:#5a2c14;
  --cocoa-mid:#7a3f1c;
  --caramel:#a4541f;
  --caramel-btn:#b5651f;
  --cream:#f4ecdc;
  --sand:#ebe0c8;
  --line:#ddd2bc;
  --text:#333;
  --muted:#666;
  --white:#fff;
}
*{box-sizing:border-box;margin:0;padding:0}
html,body{width:1200px;height:946px;overflow:hidden}
body{position:relative;background:var(--sand);font-family:"Arimo",Arial,sans-serif;color:var(--text);font-size:13px}
.header-drip{position:absolute;left:0;top:0;width:1200px;height:118px;background:linear-gradient(180deg,#2e1407 0%,#4a230f 55%,#6a3517 100%)}
.brand-plate{position:absolute;left:159px;top:0;width:251px;height:104px;background:var(--cream);display:flex;align-items:center;justify-content:center;box-shadow:0 2px 6px rgba(0,0,0,.35)}
.brand-name{font-family:"PT Serif",Georgia,serif;font-weight:700;font-size:30px;color:var(--cocoa)}
.header-tools{position:absolute;top:12px;right:150px;display:flex;gap:36px;color:var(--white);font-size:13px}
.header-tools span{display:flex;align-items:center;gap:8px}
.main-nav{position:absolute;left:0;top:114px;width:1200px;height:36px;background:var(--cocoa-dark);border-bottom:2px solid #2a1206}
.main-nav ul{list-style:none;position:absolute;left:146px;top:0;display:flex;height:36px}
.main-nav li{color:var(--white);font-size:13.5px;font-weight:700;line-height:36px;padding:0 16px;border-right:1px solid #5a2e18}
.main-nav li.active{background:var(--cocoa-mid)}
.search{position:absolute;left:828px;top:6px;width:228px;height:24px;background:var(--white);border:1px solid #999;font-size:12px;color:#999;padding:4px 6px}
.search svg{position:absolute;right:6px;top:3px}
.page-panel{position:absolute;left:141px;top:155px;width:918px;height:595px;background:var(--white);box-shadow:0 0 8px rgba(0,0,0,.2)}
.breadcrumb{position:absolute;left:20px;top:16px;font-size:12px;color:var(--muted)}
.breadcrumb b{color:var(--caramel);font-weight:400}
.page-title{position:absolute;left:20px;top:42px;width:878px;height:36px;background:linear-gradient(var(--cocoa-mid),var(--cocoa-dark));color:var(--cream);font-family:"PT Serif",Georgia,serif;font-size:22px;line-height:36px;padding-left:12px}
.steps{position:absolute;left:20px;top:120px;width:878px}
.step{height:32px;border:1px solid var(--line);background:#f6f1e6;display:flex;align-items:center;margin-bottom:0;border-top:none}
.step:first-child{border-top:1px solid var(--line)}
.step-num{width:26px;height:26px;margin:0 8px 0 3px;background:var(--caramel);color:var(--white);font-weight:700;font-size:14px;display:flex;align-items:center;justify-content:center}
.step-title{color:var(--caramel);font-weight:700;font-size:12.5px}
.step-body{height:275px;border:1px solid var(--line);border-top:none;display:flex;padding:18px 0 0}
.col{flex:1;padding:0 34px}
.col+.col{border-left:1px solid var(--line)}
.col h3{font-family:"PT Serif",Georgia,serif;font-weight:400;font-size:18px;color:var(--cocoa);margin-bottom:10px}
.col p{font-size:12px;margin-bottom:6px;line-height:1.4}
.radio{display:flex;align-items:center;gap:6px;font-size:12px;font-weight:700;margin-bottom:6px}
.radio i{width:11px;height:11px;border:1px solid #777;border-radius:50%;display:inline-block;background:var(--white)}
.radio i.on{background:radial-gradient(#2a5db0 35%,#fff 40%)}
.col ul{list-style:none;font-size:12px;margin:6px 0 20px}
.col ul li::before{content:"• "}
.btn{display:inline-block;background:var(--caramel-btn);color:var(--white);font-size:12px;font-weight:700;padding:5px 16px;border-radius:2px}
.field label{display:block;font-size:12px;font-weight:700;margin:10px 0 4px}
.field label em{color:#c00;font-style:normal}
.field div{width:284px;height:26px;border:1px solid #bbb}
.login-foot{display:flex;justify-content:space-between;align-items:center;margin-top:40px;padding-top:8px}
.login-foot a{color:var(--caramel);font-size:12px;text-decoration:underline}
.footer{position:absolute;left:0;top:760px;width:1200px;height:186px}
.f-col{position:absolute;top:10px}
.f-col h4{font-size:13.5px;color:var(--cocoa);font-weight:700;margin-bottom:12px;padding-bottom:8px;border-bottom:1px solid #d3c5a6}
.f-col ul{list-style:none;font-size:12px;color:#444;line-height:22px}
.f-col li::before{content:"» ";color:var(--caramel)}
.cat-grid{display:grid;grid-template-columns:110px 110px}
.newsletter p{font-size:11.5px;line-height:1.4;width:200px}
.news-input{width:180px;height:20px;border:1px solid #bbb;background:var(--white);font-size:11px;color:#999;padding:2px 4px;margin:10px 0 8px}
.news-btn{display:inline-block;background:var(--cocoa);color:var(--white);font-size:11px;font-weight:700;padding:4px 10px}
.f-brand{position:absolute;left:846px;top:22px;width:200px;text-align:center}
.f-brand .brand-name{font-size:26px}
.f-brand p{font-size:11.5px;color:#444;margin-top:18px;line-height:1.5}
</style>
</head>
<body>
<div class="header-drip" role="img" aria-label="Melted chocolate drip banner"></div>
<div class="brand-plate"><span class="brand-name">Maison Brunelle</span></div>
<div class="header-tools">
  <span><svg width="16" height="14" viewBox="0 0 16 14"><path d="M0 1h3l2 8h9l2-6H4" fill="none" stroke="#fff" stroke-width="1.5"/><circle cx="6" cy="12" r="1.5" fill="#fff"/><circle cx="13" cy="12" r="1.5" fill="#fff"/></svg>Shopping Cart : 0 item $0.00</span>
  <span><svg width="12" height="14" viewBox="0 0 12 14"><rect x="1" y="6" width="10" height="8" fill="#e0b34a"/><path d="M3 6V4a3 3 0 016 0v2" fill="none" stroke="#e0b34a" stroke-width="1.5"/></svg>Login / Signup</span>
</div>
<nav class="main-nav">
  <ul>
    <li class="active">Gift Boxes</li><li>Gift Baskets</li><li>Gift Trays</li><li>Dairy Free</li><li>Sugar Free</li><li>Bulk Confections</li>
  </ul>
  <div class="search">Search<svg width="16" height="16" viewBox="0 0 16 16"><circle cx="6.5" cy="6.5" r="5" fill="none" stroke="#333" stroke-width="2"/><path d="M10 10l5 5" stroke="#333" stroke-width="2"/></svg></div>
</nav>

<main class="page-panel">
  <div class="breadcrumb">Home » Shopping Cart » <b>Checkout</b></div>
  <h1 class="page-title">Checkout</h1>
  <div class="steps">
    <div class="step"><span class="step-num">1</span><span class="step-title">Checkout Method</span></div>
    <div class="step-body">
      <div class="col">
        <h3>New Customer</h3>
        <p>Select an option below to begin</p>
        <div class="radio"><i class="on"></i>Register Account</div>
        <div class="radio"><i></i>Guest Checkout</div>
        <p style="margin-top:12px"><b>Register and save time!</b><br>Register with us for future convenience:</p>
        <ul><li>Fast and easy check out</li><li>Easy access to your order history and status</li></ul>
        <span class="btn">Continue</span>
      </div>
      <div class="col">
        <h3>Login</h3>
        <p><b>Already registered?</b><br>Please log in below.</p>
        <div class="field"><label>Email Address: <em>*</em></label><div></div></div>
        <div class="field"><label>Password: <em>*</em></label><div></div></div>
        <div class="login-foot"><a>Forgot your password?</a><span class="btn">Login</span></div>
      </div>
    </div>
    <div class="step"><span class="step-num">2</span><span class="step-title">Billing Information</span></div>
    <div class="step"><span class="step-num">3</span><span class="step-title">Shipping Information</span></div>
    <div class="step"><span class="step-num">4</span><span class="step-title">Shipping Arrive on Date, Method and Gift Message</span></div>
    <div class="step"><span class="step-num">5</span><span class="step-title">Payment Information</span></div>
    <div class="step"><span class="step-num">6</span><span class="step-title">Order Review</span></div>
  </div>
</main>

<footer class="footer">
  <div class="f-col" style="left:159px"><h4>Quick Links</h4>
    <ul style="padding-left:44px"><li>About Us</li><li>Testimonials</li><li>Our Guarantee</li><li>Our Privacy Policy</li><li>Contact Us</li></ul></div>
  <div class="f-col" style="left:344px"><h4>Product Category</h4>
    <ul class="cat-grid" style="padding-left:12px"><li>Gift Boxes</li><li>Sugar Free</li><li>Gift Baskets</li><li>Bulk Confections</li><li>Gift Trays</li><li>Shipping</li><li>Dairy Free</li><li>Contact Us</li></ul></div>
  <div class="f-col newsletter" style="left:585px"><h4>Newsletter</h4>
    <p style="padding-left:10px">Subscribe to our newsletter to receive our special offers , discounts and more</p>
    <div style="padding-left:10px"><div class="news-input">Email Address</div><span class="news-btn">Subscribe</span></div></div>
  <div class="f-brand"><span class="brand-name">Maison Brunelle</span>
    <p>© Copyright 2013 Brunelle Sweets<br>All Rights Reserved</p></div>
</footer>
</body>
</html>
```